Brackwell HVAC Service LLC Business Card

We just got a design created by one of your designers for a logo and now would like help with a business card design. The information to be included on the card is as follows:
Brackwell HVAC Service LLC (I will attach logo design)
P.O. Box 418
Alder Springs, CO 80694
(970) 555-0147
Dale Vonnholt
I might include an e-mail address, but I'm not sure yet.
Target Market(s)
Customers needing service or repairs done on their heating and air conditioning systems.
Industry/Entity Type
Business
Contact Information for Business Card
P.O. Box 418
Alder Springs, CO 80694
(970) 555-0147
Dale Vonnholt

```html
<!DOCTYPE html>
<html lang="en">
<head>
<meta charset="utf-8">
<title>Brackwell HVAC Service LLC – Business Card</title>
<link rel="stylesheet" href="https://fonts.googleapis.com/css2?family=Open+Sans:wght@400;700&display=swap">
<style>
  :root {
    --stage: #e9e6e1;
    --red-light: #d0121b;
    --red-dark: #9c0c10;
    --white: #ffffff;
    --blue-light: #1d9ddb;
    --blue-dark: #0b4a8f;
    --navy: #1b2f6b;
    --text-light: #ffffff;
  }
  html, body {
    margin: 0;
    padding: 0;
    width: 1200px;
    height: 1023px;
    overflow: hidden;
    background: var(--stage);
  }
  .card {
    position: absolute;
    left: 390px;
    top: 161px;
    width: 420px;
    height: 700px;
    border-radius: 4px;
    overflow: hidden;
    box-shadow: 0 10px 30px rgba(0,0,0,0.18);
  }
  .card-background {
    position: absolute;
    inset: 0;
    display: block;
  }
  .brand {
    position: absolute;
    left: 50px;
    right: 50px;
    top: 118px;
    text-align: center;
  }
  .brand-dot {
    width: 44px;
    height: 44px;
    border-radius: 50%;
    background: var(--red-light);
    margin: 0 auto 14px;
  }
  .brand-name {
    font-family: "Open Sans", sans-serif;
    font-weight: 700;
    font-size: 28px;
    line-height: 1.15;
    color: var(--navy);
    text-transform: uppercase;
    margin: 0;
  }
  .holder-name {
    position: absolute;
    left: 0;
    right: 0;
    top: 372px;
    height: 42px;
    line-height: 42px;
    padding-left: 52px;
    font-family: "Open Sans", sans-serif;
    font-weight: 700;
    font-size: 25px;
    color: var(--text-light);
    margin: 0;
  }
  .contact-list {
    position: absolute;
    left: 44px;
    right: 20px;
    top: 452px;
    margin: 0;
    padding: 0;
    list-style: none;
    font-family: "Open Sans", sans-serif;
    font-size: 20px;
    line-height: 27px;
    color: var(--text-light);
  }
  .contact-item {
    display: flex;
    align-items: flex-start;
    gap: 12px;
    margin-bottom: 10px;
  }
  .contact-icon {
    flex: none;
    width: 20px;
    height: 20px;
    margin-top: 4px;
  }
</style>
</head>
<body>
  <article class="card">
    <svg class="card-background" viewBox="0 0 420 700" width="420" height="700" aria-hidden="true">
      <defs>
        <linearGradient id="blue-field" x1="0" y1="0" x2="0" y2="1">
          <stop offset="0.3" stop-color="#1d9ddb"/>
          <stop offset="1" stop-color="#0b4a8f"/>
        </linearGradient>
        <linearGradient id="red-field" x1="0" y1="0" x2="0" y2="1">
          <stop offset="0" stop-color="#d0121b"/>
          <stop offset="1" stop-color="#9c0c10"/>
        </linearGradient>
      </defs>
      <rect class="field-blue" width="420" height="700" fill="url(#blue-field)"/>
      <rect class="field-red" width="420" height="200" fill="url(#red-field)"/>
      <ellipse class="field-white" cx="210" cy="190" rx="300" ry="140" fill="#ffffff"/>
      <rect class="name-band" x="0" y="372" width="420" height="42" fill="#c40f18"/>
    </svg>

    <div class="brand">
      <div class="brand-dot"></div>
      <p class="brand-name">Brackwell HVAC<br>Service LLC</p>
    </div>

    <p class="holder-name">Dale Vonnholt</p>

    <ul class="contact-list">
      <li class="contact-item">
        <svg class="contact-icon" viewBox="0 0 20 20" aria-hidden="true">
          <circle cx="10" cy="10" r="10" fill="#ffffff"/>
          <path d="M10 4a4 4 0 0 0-4 4c0 3 4 8 4 8s4-5 4-8a4 4 0 0 0-4-4z" fill="#0f5ba3"/>
          <circle cx="10" cy="8" r="1.5" fill="#ffffff"/>
        </svg>
        <span>P.O. Box 418<br>Alder Springs, CO 80694</span>
      </li>
      <li class="contact-item">
        <svg class="contact-icon" viewBox="0 0 20 20" aria-hidden="true">
          <circle cx="10" cy="10" r="10" fill="#ffffff"/>
          <path d="M7 5l2 2.5-1.2 1.3c.6 1.4 1.8 2.6 3.2 3.2L12.3 11l2.5 2-1 1.8C9.5 15 5 10.5 5.2 6.2z" fill="#0f5ba3"/>
        </svg>
        <span>(970) 555-0147</span>
      </li>
      <li class="contact-item">
        <svg class="contact-icon" viewBox="0 0 20 20" aria-hidden="true">
          <circle cx="10" cy="10" r="10" fill="#ffffff"/>
          <rect x="5" y="6.5" width="10" height="7" fill="none" stroke="#0f5ba3" stroke-width="1.4"/>
          <path d="M5 6.5l5 4 5-4" fill="none" stroke="#0f5ba3" stroke-width="1.4"/>
        </svg>
        <span>dale@brackwellhvac.com</span>
      </li>
    </ul>
  </article>
</body>
</html>
```